Business card design needed

Need a new business card design for a new business in Sydney, Australia called 'Verrowin Australia'. The business deals in consulting for new sales, sales leadership and customer service consultancy. Want the business card to look professional and clean

Industry/Entity Type

Leadership

Contact Information for Business Card

Verrowin Australia
Tobias Wrenley
Managing Director

14 Quarrion Avenue
Marrowdale NSW 2041

0432 517 806
tobias@verrowin.com.au
www.verrowin.com.au

```html
<!DOCTYPE html>
<html lang="en">
<head>
<meta charset="utf-8">
<title>Verrowin Australia — Business Card</title>
<link rel="stylesheet" href="https://fonts.googleapis.com/css2?family=Arimo:wght@400&family=Open+Sans:wght@700&display=swap">
<style>
  :root {
    --card-bg: #070707;
    --text-white: #ffffff;
    --accent-red: #f0260b;
    --brand-grey: #6f7b7d;
    --tone-grey: #1a1a1a;
    --tone-brown: #1a0f0f;
    --tone-navy: #0e1236;
    --tone-blue: #1c3fc4;
    --tone-red: #f0260b;
    --tone-white: #f2f2f2;
    --card-w: 1200px;
    --card-h: 741px;
  }
  * { margin: 0; padding: 0; box-sizing: border-box; }
  html, body {
    width: var(--card-w);
    height: var(--card-h);
    overflow: hidden;
    background: var(--card-bg);
  }
  .card {
    position: relative;
    width: var(--card-w);
    height: var(--card-h);
    overflow: hidden;
    background: var(--card-bg);
    font-family: "Arimo", Arial, sans-serif;
    color: var(--text-white);
  }
  .backdrop {
    position: absolute;
    inset: 0;
    width: 100%;
    height: 100%;
  }
  .website {
    position: absolute;
    left: 21px;
    top: 37px;
    font-size: 24px;
    line-height: 28px;
    letter-spacing: 0.3px;
  }
  .person {
    position: absolute;
    right: 51px;
    top: 33px;
    text-align: right;
    font-size: 28px;
    letter-spacing: 4.4px;
    line-height: 38px;
  }
  .person-title { color: var(--accent-red); }
  .brand {
    position: absolute;
    left: 300px;
    width: 590px;
    top: 258px;
    display: flex;
    justify-content: center;
    align-items: center;
    gap: 20px;
  }
  .brand-mark {
    flex: none;
    width: 34px;
    height: 34px;
    border-radius: 50%;
    background: var(--accent-red);
  }
  .brand-name {
    font-family: "Open Sans", Arial, sans-serif;
    font-weight: 700;
    font-size: 64px;
    letter-spacing: -1px;
    color: var(--brand-grey);
    line-height: 1;
    white-space: nowrap;
  }
  .contact-line {
    position: absolute;
    left: 119px;
    top: 658px;
    font-size: 25px;
    line-height: 30px;
    letter-spacing: 0.2px;
    white-space: nowrap;
  }
</style>
</head>
<body>
  <main class="card">
    <svg class="backdrop" viewBox="0 0 1200 741" role="img" aria-label="Soft background areas where the brand's decorative illustration sits in grey, brown, navy, blue, red and white tones">
      <defs>
        <radialGradient id="glow-grey"><stop offset="0" stop-color="var(--tone-grey)"/><stop offset="1" stop-color="var(--tone-grey)" stop-opacity="0"/></radialGradient>
        <radialGradient id="glow-brown"><stop offset="0" stop-color="var(--tone-brown)"/><stop offset="1" stop-color="var(--tone-brown)" stop-opacity="0"/></radialGradient>
        <radialGradient id="glow-navy"><stop offset="0" stop-color="var(--tone-navy)"/><stop offset="1" stop-color="var(--tone-navy)" stop-opacity="0"/></radialGradient>
        <radialGradient id="glow-blue"><stop offset="0" stop-color="var(--tone-blue)" stop-opacity="0.55"/><stop offset="1" stop-color="var(--tone-blue)" stop-opacity="0"/></radialGradient>
        <radialGradient id="glow-red"><stop offset="0" stop-color="var(--tone-red)" stop-opacity="0.45"/><stop offset="1" stop-color="var(--tone-red)" stop-opacity="0"/></radialGradient>
        <radialGradient id="glow-white"><stop offset="0" stop-color="var(--tone-white)" stop-opacity="0.25"/><stop offset="1" stop-color="var(--tone-white)" stop-opacity="0"/></radialGradient>
      </defs>
      <ellipse class="area-grey" cx="370" cy="90" rx="170" ry="120" fill="url(#glow-grey)"/>
      <ellipse class="area-brown" cx="960" cy="245" rx="260" ry="200" fill="url(#glow-brown)"/>
      <ellipse class="area-navy" cx="300" cy="560" rx="400" ry="260" fill="url(#glow-navy)"/>
      <ellipse class="area-blue" cx="460" cy="470" rx="170" ry="130" fill="url(#glow-blue)"/>
      <ellipse class="area-red" cx="770" cy="420" rx="140" ry="100" fill="url(#glow-red)"/>
      <ellipse class="area-white" cx="615" cy="195" rx="90" ry="65" fill="url(#glow-white)"/>
    </svg>

    <p class="website">www.verrowin.com.au</p>
    <div class="person">
      <p class="person-name">Tobias Wrenley</p>
      <p class="person-title">Managing Director</p>
    </div>
    <div class="brand">
      <span class="brand-mark" aria-hidden="true"></span>
      <span class="brand-name">Verrowin Australia</span>
    </div>
    <p class="contact-line">14 Quarrion Avenue Marrowdale NSW 2041 0432 517 806 tobias@verrowin.com.au</p>
  </main>
</body>
</html>
```